Website for IT Security Company in Austria with small and medium business customer base

I own a one man IT security company with a customer small to medium business customer base and need a professional looking website that contains the following information:
- Home page: About the company....
- Services: The services that I offer. It would be nice to have icons if possible (e.g Quorel Ledger icon, digital certificate icon, ...) but this is not a must have.
- About me
- Blog: This is not a must have. It would be ok to just link it to an external blog.
- Impressum
- Contact: No form, just telephone number and e-mail address
- Anything else that you think is necessary for a professional appearance
Also I attached the company design. I do have all source files for the logo if required.

Target Market(s)

Small and medium business of all branches located in Austria

Industry/Entity Type

Cyber Security

Coding

Coded - Design and coding required

Number of Pages Required

5+ page

Font styles to use
Serif
Sans Serif
Other font styles liked:
• Bitsumishi, Bankgothic

Colors

Designer to choose only greyscale colors for use in the design.

Requirements
Must have
• The website must be a mobile-first design.
The design should not be too colorful or playful.
The logo should be used as much as possible
Navigation bar with multi drop-down menu for the services that I offer.
Example:
Services
-> Implementations
-> Implementation Service A
-> Implementation Service B
-> Security Audit
-> Audit A
-> Audit B
Maybe you could have service cards that describe the services briefly and on click redirect to the site that describes the service in detail.
End of example
Logo
contact
impressum
services that I offer
about me
about the company
Nice to have
• Icons would be nice (e.g. house for homepage, letter for contact, ...)
Also for the services I offer icons would be nice (Quorel Ledger, digtial certificates, hacking, security auditing)
For the fonts I have only sugested Bitsumishi and Bankgothic as they are part of my logo. No sure if you feel they make sense as part of the website
Should not have
• forms.
I want to the site to be made as easy as possible (HTML5, CSS, javascript/php/.net)
I do not want a wordpress template or suchlike.

```html
<!DOCTYPE html>
<html lang="en">
<head>
<meta charset="utf-8">
<title>Graphite Bastion – IT Security</title>
<link href="https://fonts.googleapis.com/css2?family=Michroma&family=Roboto:wght@400&display=swap" rel="stylesheet">
<style>
:root{
  --black:#000;
  --ink:#1d1d1d;
  --text:#666;
  --muted:#888;
  --line:#e6e6e6;
  --white:#fff;
  --hero-a:#9a9a9a;
  --hero-b:#5e5e5e;
  --band-a:#1a2236;
  --band-b:#2b3346;
}
*{margin:0;padding:0;box-sizing:border-box}
html,body{width:1200px;height:3166px;overflow:hidden}
body{position:relative;background:var(--white);font-family:"Roboto",Arial,sans-serif;color:var(--text)}
.display{font-family:"Michroma",sans-serif}
.abs{position:absolute}

.site-header{left:0;top:0;width:1200px;height:138px;background:var(--black)}
.brand{display:flex;align-items:center;gap:10px;color:var(--white);font-family:"Michroma",sans-serif;font-size:17px;letter-spacing:1px}
.brand-mark{width:16px;height:16px;background:var(--white)}
.site-header .brand{position:absolute;left:111px;top:58px}
.main-nav{position:absolute;left:432px;top:66px;display:flex;gap:35px}
.main-nav a{color:var(--white);text-decoration:none;font-family:"Michroma",sans-serif;font-size:12.5px}

.hero{left:0;top:138px;width:1200px;height:741px;background:radial-gradient(ellipse at 50% 45%,var(--hero-a),var(--hero-b) 75%,#3e3e3e)}
.hero-title{left:0;top:425px;width:1200px;text-align:center;color:var(--white);font-family:"Michroma",sans-serif;font-size:58px;letter-spacing:2px}
.hero-sub{left:0;top:515px;width:1200px;text-align:center;color:var(--white);font-family:"Michroma",sans-serif;font-size:24px;letter-spacing:36px;padding-left:36px}
.btn{display:flex;align-items:center;justify-content:center;border-radius:30px;font-family:"Michroma",sans-serif;font-size:13px;text-decoration:none}
.btn-ghost-light{border:2px solid var(--white);color:var(--white)}
.btn-ghost-dark{border:1px solid #999;color:#555;font-size:12px}
.btn-solid{background:var(--ink);color:var(--white)}

.service-card{top:802px;width:308px;height:339px;background:var(--white);border:1px solid var(--line);border-radius:8px;box-shadow:0 2px 6px rgba(0,0,0,.05);padding:0 32px}
.service-card svg{margin-top:26px}
.service-card h3{font-family:"Michroma",sans-serif;font-weight:400;font-size:15px;color:#222;margin-top:14px}
.service-card p{font-size:13.5px;line-height:26.5px;margin-top:18px;text-align:justify}
.service-card .btn{width:135px;height:47px;margin-top:22px}

.about-heading{left:111px;top:1238px;font-family:"Michroma",sans-serif;font-size:28px;color:var(--ink)}
.about-lead{left:111px;top:1288px;width:420px;font-size:21px;line-height:31px;color:#555}
.about-text{left:111px;top:1361px;width:410px;font-size:14px;line-height:25.8px;text-align:justify}
.about-photo{left:579px;top:1223px;width:510px;height:405px;background:linear-gradient(135deg,#6f6f6f,#3a3a3a 55%,#262626);border-radius:2px}

.feature-band{left:0;top:1699px;width:1200px;height:505px;background:linear-gradient(100deg,var(--band-a),var(--band-b) 60%,#3b3e45)}
.feature-title{left:111px;top:1808px;color:var(--white);font-family:"Michroma",sans-serif;font-size:19px;line-height:39px}
.feature-text{left:111px;top:1894px;width:410px;color:#e2e2e2;font-size:15px;line-height:30px}

.section-title{left:0;top:2275px;width:1200px;text-align:center;font-family:"Michroma",sans-serif;font-size:27px;color:#333}
.title-rule{left:577px;top:2323px;width:46px;height:2px;background:var(--ink)}

.blog-card{top:2358px;width:314px;height:423px;background:var(--white);border:1px solid var(--line);border-radius:8px;box-shadow:0 2px 6px rgba(0,0,0,.06);overflow:hidden;text-align:center}
.blog-image{height:230px}
.date-badge{position:absolute;left:113px;top:186px;width:88px;height:88px;border-radius:50%;background:var(--ink);border:3px solid var(--white);color:var(--white);font-family:"Michroma",sans-serif;font-size:17px;line-height:22px;display:flex;flex-direction:column;justify-content:center}
.blog-card h4{font-family:"Michroma",sans-serif;font-weight:400;font-size:15.5px;color:#333;margin-top:60px}
.blog-card p{font-size:13.5px;line-height:25px;margin:16px 22px 0;color:var(--muted)}

.site-footer{left:0;top:2855px;width:1200px;height:311px;background:var(--black);color:var(--white)}
.site-footer .brand{position:absolute;left:0;top:68px;width:1200px;justify-content:center;font-size:20px}
.footer-contact{left:0;top:173px;width:1200px;text-align:center;font-family:"Michroma",sans-serif;font-size:14px}
.footer-contact span{margin:0 38px}
.copyright{left:0;top:237px;width:1200px;text-align:center;font-size:15px}
</style>
</head>
<body>

<header class="site-header abs">
  <div class="brand"><span class="brand-mark"></span>GRAPHITE BASTION</div>
  <nav class="main-nav">
    <a href="#">HOME</a><a href="#">ABOUT ME</a><a href="#">SERVICES</a><a href="#">BLOG</a><a href="#">IMPRESSUM</a><a href="#">CONTACT US</a>
  </nav>
</header>

<section class="hero abs" role="img" aria-label="Grey city skyline under a network of connected nodes around a padlock"></section>
<h1 class="hero-title abs">GRAPHITE BASTION</h1>
<div class="hero-sub abs">IT SECURITY</div>
<a class="btn btn-ghost-light abs" href="#" style="left:509px;top:580px;width:182px;height:56px">READ MORE</a>

<article class="service-card abs" style="left:111px">
  <svg width="76" height="80" viewBox="0 0 76 80" fill="none" stroke="#333" stroke-width="2">
    <rect x="2" y="20" width="56" height="56"/><rect x="12" y="44" width="16" height="14"/><rect x="34" y="52" width="16" height="14"/><path d="M28 51h6"/>
    <circle cx="54" cy="22" r="10" fill="#fff"/><circle cx="54" cy="22" r="4"/>
  </svg>
  <h3>IMPLEMENTATIONS</h3>
  <p>Sed ut perspiciatis unde omnis iste nat us error sit voluptatem accusanti um bea vita dicta sunt explicabo.</p>
  <a class="btn btn-ghost-dark" href="#">READ MORE</a>
</article>
<article class="service-card abs" style="left:446px">
  <svg width="70" height="80" viewBox="0 0 70 80" fill="none" stroke="#333" stroke-width="2">
    <path d="M4 20 Q35 -6 66 20 Z"/><path d="M35 7v15"/>
    <rect x="12" y="26" width="46" height="52" rx="3"/><path d="M20 40h22M20 52h22M20 64h22M48 38l3 3 5-5M48 50l3 3 5-5M48 62l3 3 5-5"/>
  </svg>
  <h3>SECURITY AUDIT</h3>
  <p>Sed ut perspiciatis unde omnis iste nat us error sit voluptatem accusanti um bea vita dicta sunt explicabo.</p>
  <a class="btn btn-ghost-dark" href="#">READ MORE</a>
</article>
<article class="service-card abs" style="left:781px">
  <svg width="76" height="80" viewBox="0 0 76 80" fill="none" stroke="#333" stroke-width="2">
    <path d="M38 14l14 8v16l-14 8-14-8V22z M24 22l14 8 14-8 M38 30v16"/>
    <path d="M24 38l14 8v16l-14 8-14-8V46z M10 46l14 8 14-8 M24 54v16"/>
    <path d="M52 38l14 8v16l-14 8-14-8V46z M38 46l14 8 14-8 M52 54v16"/>
  </svg>
  <h3>OTHER</h3>
  <p>Sed ut perspiciatis unde omnis iste nat us error sit voluptatem accusanti um bea vita dicta sunt explicabo.</p>
  <a class="btn btn-ghost-dark" href="#">READ MORE</a>
</article>

<h2 class="about-heading abs">ABOUT ME</h2>
<p class="about-lead abs">Sed ut perspiciatis unde omnis iste natus error sit voluptatem</p>
<p class="about-text abs">Nemo enim ipsam voluptatem quia voluptas sit aspernatur aut odit aut fugit, sed quia consequuntur magni dolores eos qui ratione voluptatem sequi nesciunt. Neque porro quisquam est, qui dolorem ipsum quia dolor sit amet, consectetur, adipisci velit, sed quia non numquam eius modi tempora incidunt ut lab ore et dolore magnam aliquam quaerat voluptatem. Ut enim ad ullam corporis suscipit laboriosam, nisi ut aliquid...</p>
<a class="btn btn-solid abs" href="#" style="left:112px;top:1565px;width:157px;height:57px">READ MORE</a>
<div class="about-photo abs" role="img" aria-label="Security guard in a dark suit and sunglasses speaking into a radio outdoors"></div>

<section class="feature-band abs" role="img" aria-label="Hands typing on a laptop with a glowing padlock and binary code overlay"></section>
<h2 class="feature-title abs">SED UT PERSPICIATIS<br>UNDE OMNIS ISTE NATUS ERROR</h2>
<p class="feature-text abs">Nemo enim ipsam voluptatem quia voluptas sit aspern at ur aut odit aut fugit, sed quia consequuntur magni dol eos qui ratione voluptatem sequi nesciunt.</p>
<a class="btn btn-ghost-light abs" href="#" style="left:111px;top:2006px;width:160px;height:56px">READ MORE</a>

<h2 class="section-title abs">LATEST BLOG</h2>
<div class="title-rule abs"></div>

<article class="blog-card abs" style="left:111px">
  <div class="blog-image" role="img" aria-label="Hands on a keyboard with glowing hexagon security icons" style="background:linear-gradient(135deg,#3a6a86,#16283a)"></div>
  <div class="date-badge">02<span>FEB</span></div>
  <h4>SED UT PERSPICIATIS</h4>
  <p>Nemo enim ipsam voluptatem quia volup sit aspernatur aut odit aut fugit, sed quia co ratione voluptatem sequi nesciunt.</p>
</article>
<article class="blog-card abs" style="left:443px">
  <div class="blog-image" role="img" aria-label="Team working at monitors in a security operations room" style="background:linear-gradient(135deg,#2c4660,#0f1a26)"></div>
  <div class="date-badge">02<span>FEB</span></div>
  <h4>SED UT PERSPICIATIS</h4>
  <p>Nemo enim ipsam voluptatem quia volup sit aspernatur aut odit aut fugit, sed quia co ratione voluptatem sequi nesciunt.</p>
</article>
<article class="blog-card abs" style="left:775px">
  <div class="blog-image" role="img" aria-label="Laptop with a holographic padlock and password fields" style="background:linear-gradient(135deg,#2a2f5a,#6a4a4a 70%,#9a6a3a)"></div>
  <div class="date-badge">02<span>FEB</span></div>
  <h4>SED UT PERSPICIATIS</h4>
  <p>Nemo enim ipsam voluptatem quia volup sit aspernatur aut odit aut fugit, sed quia co ratione voluptatem sequi nesciunt.</p>
</article>

<footer class="site-footer abs">
  <div class="brand"><span class="brand-mark"></span>GRAPHITE BASTION</div>
  <div class="footer-contact abs">CALL US : 000-555-0147<span>/</span>EMAIL : info@graphitebastion.com</div>
  <div class="copyright abs">© 2021 Copyright Graphite Bastion.All Rights Reserved</div>
</footer>

</body>
</html>
```